Luxury Property Rental and Management Website (10 Pages)

1.General Requirements
1.1. Bootstrap Template
1.2. Use Ajax for dynamic data elements

2. Home Page
2.1 Main Menu - About, Destinations, Concierge, Owners & Agents, Sales, Social, Contact Us (all pages)
2.2. Main Image Carousel with headline showing feature properties (images and content in CMS)
2.3. Destinations Menu - Drop Down shows list of Markets. Also "Where Do you Want to Go" ends up at Desination Page
2.4. Contact Us Menu - Show phone number next to it and drop down with details
2.4. About QOV Holdings Content (TBD) from About Page
2.5. Testimonials / Reviews Scroller (CMS)
2.5. Contact Information with Social Media Links at Bottom (all pages)

3. Destination Page
3.1 Landing Page specfic for each market type (QOVHoldings.example/Miami, QOVHoldings.example/StBarths)
3.2. Destination page Carousel showing images and tag lines from featured properties (images and content in CMS)
3.3. Destination Specific Content - About Destination? What is Going On? What To Do? (drop down like plush havens)
3.4. Show search options (Area_Type, Property_Category, Arrival_Date, Departure_Date, Bedrooms, Amenity_List) using SearchProperty service
3.5. Show Image + footer (Name, Tag Line, Area, Bedrooms, Pricing From)
3.6. Add to Favorties
3.7. Click to open Property Page

4. Property Page
4.1 Dynamic Page specfic for each Property (QOVHoldings.example/QOV4826, QOVHoldings.example/QOV5174) using detailProperty service
4.1.1 Show Property Image Carcousel (from detailProperty service)
4.2. Show Name, Tagline, Location, Beds, Bathrooms, Location Type
4.3. Include Pricing Per Night, Per Week,Per Month with calculator and currency transloator, USD, EURO and Pound (see TO Merle)
4.4. Show Description with more
4.5 Show Details section with tab Bar - Photos, Location, Amenities, Rates
4.6. Click button to Inquire Now and to send download PDF based on page

5. Inquiry Page
5.1. Popup Page
5.2 Optional Login, Forgoet Password, or Create New User Account (choose password)
"5.3. Capture First_Name, Last_Name, Company Name (optional), Email, Phone_Number, Market_Type (fill from search) Area_Type_List (fill from search), Property_Category, Nightly_Budget, Number_Adults,Number_Children, Arrival_Date, Departure_Date, Amenity_List,Request_Note) - default Lead Source & Campaign_Id based on passed to orginal tags page on search, Type=Booking
"
5.4. Display table of Properties with Small Images, Name, Tag Line, Bedroom, Pricing based on Favorites. Delete any property and mark Top Choice making number one. Pass top Choice as Listing_Id and remaining as Alternate_Listing_id to createNewOpportunity

6. Owner & Agent Page
6.1. Display Static Content from CMS (TBD)
"5.3. Capture First_Name, Last_Name, Email, Phone_Number, Market_Type, Area_Type_List, Property_Category, Nightly_Budget, Number_Adults, Request_Note) - default Lead Source & Campaign_Id based on passed to orginal tags page on search, Type=Listing
"

7. Social Page
7.1. Display Blog Content From CMS Tagged to Market Type
7.2 Display Instagram and Facebook, Pinterest, Twitter Content

8. About Us Page
8.1. Display Static Content from CMS (TBD)
8.2. New Partner Application
8.3. Estate Journey Circle

9. Concierge Page
9.1 Define Static Content from CMS (TBD)

10. Sales Page
10.1 Define Static Content from CMS (TBD)
10.2 Incorporate dynamic property listings

Target Market(s)

High net worth travelers around the globe

Requirements
Must have
• Bootstrap and AJAX support
Nice to have
• See company presentation for an idea to look and feel
• Also these two sites have nice a approach.
• www.tomerle.example
• www.PlushHavens.example

```html
<!DOCTYPE html>
<html lang="en">
<head>
<meta charset="utf-8">
<title>QOV Holdings</title>
<link href="https://fonts.googleapis.com/css2?family=Crimson+Text:wght@400;600&family=Open+Sans:ital,wght@0,400;0,600;1,400&display=swap" rel="stylesheet">
<style>
:root{
  --black:#050505;
  --gold:#d9a22b;
  --gold-light:#e8b43c;
  --gold-dark:#b9780d;
  --gold-text:#c98a1c;
  --white:#ffffff;
  --grey-bg:#f6f6f6;
  --card-border:#e2e2e2;
  --text:#555555;
  --muted:#8a8a8a;
  --footer:#1c1c1c;
  --footer-bottom:#141414;
}
*{margin:0;padding:0;box-sizing:border-box}
html,body{width:1200px;height:2190px;overflow:hidden}
body{font-family:"Open Sans",sans-serif;color:var(--text);background:var(--white);position:relative}
.serif{font-family:"Crimson Text",serif}

.site-header{height:105px;background:var(--black);position:relative}
.brand{position:absolute;left:117px;top:24px;display:flex;align-items:center;gap:12px}
.brand-mark{width:52px;height:52px;border:2px solid var(--gold);border-radius:50%}
.brand-name{color:var(--gold);font-size:19px}
.call{position:absolute;right:101px;top:32px;text-align:right}
.call-label{color:var(--white);font-size:15px;letter-spacing:.3px}
.call-number{color:var(--gold-light);font-size:22px;font-weight:600;margin-top:2px}

.main-nav{height:50px;background:linear-gradient(#e6b13a,#c98d1a);display:flex;justify-content:center;padding-left:10px;border-bottom:1px solid #a77010}
.main-nav a{color:var(--white);text-decoration:none;font-size:16px;font-weight:600;line-height:50px;padding:0 21px;border-right:1px solid rgba(120,70,0,.45)}
.main-nav a:last-child{border-right:none}

.hero{position:relative;height:440px;background:linear-gradient(160deg,#1b2460 0%,#3a4a8a 35%,#9a7cb0 55%,#c46a6a 75%,#263a55 100%)}
.hero-caption{position:absolute;left:100px;top:128px;width:455px;height:160px;background:rgba(0,0,0,.72);clip-path:polygon(0 0,100% 0,90% 100%,0 100%);padding:20px 0 0 33px}
.hero-title{color:var(--gold-light);font-size:42px;line-height:1}
.hero-sub{color:var(--white);font-size:25px;margin-top:6px}
.hero-text{color:#9a9a9a;font-size:12px;line-height:19px;margin-top:6px;width:345px}
.dots{position:absolute;left:573px;bottom:10px;display:flex;gap:4px}
.dots span{width:16px;height:16px;border-radius:50%;background:#2a2a2a}

.welcome{height:200px;text-align:center;padding-top:33px}
.welcome h1{font-weight:400;font-size:35px;color:#222}
.welcome p{font-size:12.5px;line-height:22px;color:#555;margin:8px auto 0;width:1000px}

.destinations{height:780px;background:var(--grey-bg);border-top:1px solid #ececec;border-bottom:1px solid #dcdcdc;padding-top:22px}
.section-title{text-align:center;font-weight:400;font-size:34px;color:var(--gold-text)}
.grid{display:grid;grid-template-columns:repeat(4,242px);gap:12px 11px;margin:22px 0 0 100px}
.card{height:208px;background:var(--white);border:1px solid var(--card-border);padding:9px}
.card-img{height:110px}
.card h3{color:var(--gold-text);font-weight:600;font-size:15px;margin:8px 0 0 5px}
.card p{font-size:11.5px;line-height:19px;color:var(--muted);margin:3px 0 0 5px}

.testimonials{height:310px;background:linear-gradient(#e2ac33,#c68712);position:relative;text-align:center;padding-top:34px}
.testimonials h2{color:var(--white);font-weight:400;font-size:27px}
.quotes{display:flex;margin:34px 0 0 110px}
.quote{display:flex;width:340px;padding-right:14px;border-right:1px solid rgba(255,255,255,.25);margin-right:2px;text-align:left}
.quote:last-child{border-right:none}
.avatar{width:92px;height:92px;border-radius:50%;border:4px solid var(--white);flex:none;margin-right:18px}
.quote p{font-style:italic;font-size:12px;line-height:19px;color:var(--white)}
.quote .author{font-style:normal;font-weight:600;font-size:12.5px;margin-top:6px}
.arrows{position:absolute;left:1052px;top:262px}

.site-footer{height:245px;background:linear-gradient(#2a2a2a,#111);display:flex;padding:36px 0 0 104px}
.footer-col{color:#ddd}
.footer-col h4{font-weight:400;font-size:22px;color:#eee;margin-bottom:4px}
.footer-col li{list-style:none;font-size:13px;line-height:26px;padding-left:2px}
.col-company{width:214px}.col-support{width:197px}.col-links{width:217px}
.social{display:flex;gap:10px;margin-top:8px}
.social span{width:24px;height:24px;border-radius:3px}
.bottom-bar{height:60px;background:var(--footer-bottom);color:#444;font-size:12px;padding:18px 0 0 100px}
</style>
</head>
<body>
<header class="site-header">
  <div class="brand"><span class="brand-mark"></span><span class="brand-name">QOV Holdings</span></div>
  <div class="call"><div class="call-label">CALL US NOW</div><div class="call-number">+1-555-310-7284</div></div>
</header>
<nav class="main-nav">
  <a href="#">HOME</a><a href="#">ABOUT</a><a href="#">DESTINATIONS</a><a href="#">CONCIERGE</a><a href="#">OWNERS &amp; AGENTS</a><a href="#">SALES</a><a href="#">SOCIAL</a><a href="#">CONTACT US</a>
</nav>

<section class="hero" role="img" aria-label="Photo of a curved luxury beachfront hotel at dusk with a lit pool and palm trees">
  <div class="hero-caption">
    <div class="hero-title serif">Featured Properties</div>
    <div class="hero-sub serif">Suspendisse vulputate aliquam</div>
    <div class="hero-text">Etiam est nunc venenatis in tristique eu imperdiet ac nisl. Cum sociis natoque penatibus et magnis dis part</div>
  </div>
  <div class="dots"><span></span><span></span><span></span></div>
</section>

<section class="welcome">
  <h1 class="serif">Welcome to QOV Holdings Mainpage</h1>
  <p>QOV Holdings is everywhere you need to be! Short term rentals, vacation property rentals and property management are just some of the services we offer at QOV.<br>Get access to both short &amp; long term property rentals at the best prices with top-notch support from our team. Browse through our variety of cities worldwide and find your perfectly furnished short term stay today. Our new Global Partners Program can now serve you better with our specialized local teams in each specific location.</p>
</section>

<section class="destinations">
  <h2 class="section-title serif">Top Destination</h2>
  <div class="grid">
    <div class="card"><div class="card-img" role="img" aria-label="Snowy Alps mountain peaks" style="background:linear-gradient(#6d8fc0,#d9e2ee 60%,#6b7686)"></div><h3>Alps</h3><p>Morbi diam mauris viverra in gravida eu mattis in ante Morbi eget arc</p></div>
    <div class="card"><div class="card-img" role="img" aria-label="Amsterdam canal houses at dusk" style="background:linear-gradient(#6a4a9a,#b5533a 60%,#3a2418)"></div><h3>Amsterdam</h3><p>Morbi diam mauris viverra in gravida eu mattis in ante Morbi eget arc</p></div>
    <div class="card"><div class="card-img" role="img" aria-label="Bahamas beach with parasol" style="background:linear-gradient(#5fb6e6,#bfe8f2 55%,#efe6d2)"></div><h3>Bahamas</h3><p>Morbi diam mauris viverra in gravida eu mattis in ante Morbi eget arc</p></div>
    <div class="card"><div class="card-img" role="img" aria-label="Cannes seafront and harbour" style="background:linear-gradient(#7fb2e0,#e8d8c0 50%,#2a78b8)"></div><h3>Cannes</h3><p>Morbi diam mauris viverra in gravida eu mattis in ante Morbi eget arc</p></div>
    <div class="card"><div class="card-img" role="img" aria-label="New York City skyline" style="background:linear-gradient(#a8c4de,#8a8e94 55%,#4a4e54)"></div><h3>Corp NY Stay</h3><p>Morbi diam mauris viverra in gravida eu mattis in ante Morbi eget arc</p></div>
    <div class="card"><div class="card-img" role="img" aria-label="Formal garden in the Hamptons" style="background:linear-gradient(#d6e4ea,#6a8c3a 45%,#3e5a24)"></div><h3>Hampton</h3><p>Morbi diam mauris viverra in gravida eu mattis in ante Morbi eget arc</p></div>
    <div class="card"><div class="card-img" role="img" aria-label="Ibiza coastline seen from a terrace" style="background:linear-gradient(#3d7fc4,#eaeef2 45%,#2b5d8a)"></div><h3>Ibiza</h3><p>Morbi diam mauris viverra in gravida eu mattis in ante Morbi eget arc</p></div>
    <div class="card"><div class="card-img" role="img" aria-label="Las Vegas strip at night" style="background:linear-gradient(#2a3a6a,#c2782a 55%,#3a2416)"></div><h3>Las Vegas</h3><p>Morbi diam mauris viverra in gravida eu mattis in ante Morbi eget arc</p></div>
    <div class="card"><div class="card-img" role="img" aria-label="London fountain at night" style="background:linear-gradient(#1a3a6a,#2a6a9a 55%,#0e1e34)"></div><h3>London</h3><p>Morbi diam mauris viverra in gravida eu mattis in ante Morbi eget arc</p></div>
    <div class="card"><div class="card-img" role="img" aria-label="Los Angeles skyline at sunset" style="background:linear-gradient(#e6a45a,#a07a5a 55%,#5a4a3e)"></div><h3>Los Angeles</h3><p>Morbi diam mauris viverra in gravida eu mattis in ante Morbi eget arc</p></div>
    <div class="card"><div class="card-img" role="img" aria-label="Marbella marina with yachts" style="background:linear-gradient(#8ab6e0,#e8eef2 55%,#6a8ca8)"></div><h3>Marbella</h3><p>Morbi diam mauris viverra in gravida eu mattis in ante Morbi eget arc</p></div>
    <div class="card"><div class="card-img" role="img" aria-label="Miami Beach lifeguard tower" style="background:linear-gradient(#3a7cc6,#b9d6ee 55%,#e8dcc0)"></div><h3>Maimi Beach</h3><p>Morbi diam mauris viverra in gravida eu mattis in ante Morbi eget arc</p></div>
  </div>
</section>

<section class="testimonials">
  <h2>Customer Testimonials</h2>
  <div class="quotes">
    <div class="quote"><div class="avatar" role="img" aria-label="Customer portrait" style="background:#b88a6a"></div><div><p>Malesuada nec ultricies sit amet porttitor mattis enim In massa libero interdum nec interdum vel blandit sed nulla In ullamcorper est eget tempor cursus</p><p class="author">By Author Name</p></div></div>
    <div class="quote"><div class="avatar" role="img" aria-label="Customer portrait" style="background:#6a8cb0"></div><div><p>Malesuada nec ultricies sit amet porttitor mattis enim In massa libero interdum nec interdum vel blandit sed nulla In ullamcorper est eget tempor cursus</p><p class="author">By Author Name</p></div></div>
    <div class="quote"><div class="avatar" role="img" aria-label="Customer portrait" style="background:#9a8a7a"></div><div><p>Malesuada nec ultricies sit amet porttitor mattis enim In massa libero interdum nec interdum vel blandit sed nulla In ullamcorper est eget tempor cursus</p><p class="author">By Author Name</p></div></div>
  </div>
  <svg class="arrows" width="34" height="24" viewBox="0 0 34 24" aria-label="Previous and next"><path d="M10 3 L3 12 L10 21 M24 3 L31 12 L24 21" fill="none" stroke="#fff" stroke-width="2.5"/></svg>
</section>

<footer class="site-footer">
  <div class="footer-col col-company"><h4>Company</h4><ul><li>About</li><li>Destinations</li><li>Concierge</li><li>Owners &amp; Agents</li><li>Sales</li></ul></div>
  <div class="footer-col col-support"><h4>Support</h4><ul><li>Support</li><li>Social</li><li>Services</li><li>Contact Us</li></ul></div>
  <div class="footer-col col-links"><h4>Sub links</h4><ul><li>Testimonials</li><li>Recent Blog</li><li>Clients &amp; Partners</li><li>Newsletters</li></ul></div>
  <div class="footer-col"><h4>Contact Us</h4><ul><li>418 Harbor Lane,</li><li>9th Floor, Northport, NY 10990</li><li>Tel: +1 (555) 628-4190</li><li>Email: booking@qovholdings.example</li></ul>
    <div class="social"><span style="background:#3b5b9a"></span><span style="background:#38a8dc"></span><span style="background:#1e78b4"></span><span style="background:#e8781e"></span></div>
  </div>
</footer>
<div class="bottom-bar">© 2013 Company Name . All right reserved</div>
</body>
</html>
```